Dunmore Hale Voss LLC letterhead/envelope/stationary

Design letterhead and envelope based on prior logo design. Design should be conservative and classic for a defense litigation law firm.

Target Market(s)

Businesses, insurance carriers, construction companies, product manufacturers, healthcare providers, employers, municipalities. In short, the target is businesses that may be sued in court and need civil defense attorneys.

Font styles to use
Serif
Sans Serif

Colors
0255a3

Requirements
Must have
• Straightforward design for letterhead and envelopes including digital format for word. Template should be able to be updated for individual attorneys within the firm. Font should be Trajan Pro if possible to match logo (or a similar font). Firm information is Dunmore Hale Voss LLC, 4700 Westfield Terrace, Suite 320, Birmingham, Alabama, 35817. (205)368-2941. other fields that should be included are fax line, direct line, cell phone and email address so that we can update template for each attorney. The color for the logo is 003362
Nice to have
• digital template for microsoft outlook
Should not have
• Busy design/too many graphics

```html
<!DOCTYPE html>
<html lang="en">
<head>
<meta charset="utf-8">
<title>Dunmore Hale Voss LLC — Letterhead and Envelope</title>
<link href="https://fonts.googleapis.com/css2?family=Cinzel:wght@400;600&family=Lora:wght@400&family=Open+Sans:wght@400&display=swap" rel="stylesheet">
<style>
  :root {
    --navy: #003362;
    --paper: #f4f4f4;
    --canvas: #ffffff;
    --ink: #4a4a4a;
    --ink-dark: #111111;
    --shadow: rgba(0, 0, 0, 0.55);
  }
  * { margin: 0; padding: 0; box-sizing: border-box; }
  html, body { width: 1200px; height: 800px; overflow: hidden; background: var(--canvas); }
  .canvas { position: relative; width: 1200px; height: 800px; }

  .sheet {
    position: absolute;
    background: var(--paper);
    box-shadow: -12px 12px 10px var(--shadow);
  }

  /* Letterhead */
  .letterhead { left: 34px; top: 29px; width: 524px; height: 739px; }
  .letterhead .footer-band {
    position: absolute; left: 0; bottom: 0; width: 100%; height: 16px; background: var(--navy);
  }
  .firm-name {
    position: absolute;
    font-family: "Cinzel", serif; font-weight: 600; color: var(--navy);
    line-height: 1.05;
  }
  .letterhead .firm-name { left: 40px; top: 62px; font-size: 15px; width: 140px; }
  .attorney-name {
    position: absolute; left: 222px; top: 68px;
    font-family: "Cinzel", serif; font-weight: 600; font-size: 16px; color: var(--navy);
    letter-spacing: 0.2px;
  }
  .contact {
    position: absolute; left: 39px; top: 171px;
    font-family: "Lora", serif; font-size: 7.4px; line-height: 9.2px;
    font-variant: small-caps; color: var(--ink); letter-spacing: 0.2px;
  }
  .side-tag {
    position: absolute; left: 34px; top: 576px;
    transform: rotate(-90deg); transform-origin: left top;
    white-space: nowrap;
    font-family: "Cinzel", serif; font-size: 10.5px; color: var(--navy); letter-spacing: 0.4px;
  }
  .letter-body {
    position: absolute; left: 222px; top: 168px; width: 272px;
    font-family: "Lora", serif; font-size: 10.1px; line-height: 15.9px; color: var(--ink);
  }
  .salutation { font-variant: small-caps; font-size: 10.6px; color: var(--ink); margin-bottom: 23px; }
  .letter-body p { margin-bottom: 15.9px; }
  .closing { margin-top: 31px; }
  .signature { margin-top: 47px; line-height: 13px; }

  /* Envelope */
  .envelope { left: 600px; top: 29px; width: 578px; height: 269px; }
  .envelope .side-band {
    position: absolute; right: 0; top: 0; width: 13px; height: 100%; background: var(--navy);
  }
  .envelope .firm-name { left: 46px; top: 37px; font-size: 13px; width: 120px; }
  .return-address {
    position: absolute; left: 46px; top: 100px;
    font-family: "Open Sans", sans-serif; font-size: 6.6px; line-height: 8.4px; color: var(--ink-dark);
  }

  /* Presentation title */
  .title {
    position: absolute; left: 677px; top: 385px; width: 400px; text-align: center;
    font-family: "Cinzel", serif; font-weight: 400; color: var(--ink-dark);
    font-size: 46px; line-height: 44px; letter-spacing: 2px;
  }
  .tagline {
    position: absolute; left: 627px; top: 697px; width: 500px; text-align: center;
    font-family: "Cinzel", serif; font-size: 18px; color: var(--ink-dark); letter-spacing: 1.2px;
  }
</style>
</head>
<body>
<main class="canvas">

  <section class="sheet letterhead" aria-label="Letterhead">
    <div class="firm-name">Dunmore Hale Voss</div>
    <div class="attorney-name">NOLAN REED</div>

    <address class="contact">
      4700 Westfield Terrace,<br>
      Suite 320,<br>
      Birmingham, Alabama, 35817<br>
      (205)368-2941<br>
      Fax: 20536 829 40<br>
      Direct: 2053682 9414 112<br>
      Cell: 20555 4418230<br>
      Email: nolan@dhvlegal.com
    </address>

    <div class="side-tag">Dunmore Hale Voss LLC &nbsp;|&nbsp; ATTORNEYS AT LAW</div>

    <article class="letter-body">
      <div class="salutation">Dear Mr. Hale,</div>
      <p>A letterhead is the heading at the top of a sheet of letter paper (stationery). That heading usually consists of a name and an address, and a logo or corporate design, and sometimes a background pattern.</p>
      <p>The term "letterhead" is often used to refer to the whole sheet imprinted with such a heading. Many companies and individuals prefer to create a letterhead template in a word processor or other software application. This generally includes the same information as pre-printed stationery but without the additional costs involved.</p>
      <p>Letterhead can then be printed on stationery (or plain paper) as needed on a local output device or sent electronically. That heading usually consists of a name and an address, and a logo or corporate design, and sometimes a background pattern.</p>
      <p>This generally includes the same information as pre-printed stationery but without the additional costs involved.</p>
      <div class="closing">Respectfully yours,</div>
      <div class="signature">Nolan Reed<br>Attorney</div>
    </article>

    <div class="footer-band"></div>
  </section>

  <section class="sheet envelope" aria-label="Envelope">
    <div class="firm-name">Dunmore Hale Voss</div>
    <address class="return-address">
      4700 Westfield Terrace,<br>
      Suite 320,<br>
      Birmingham, Alabama, 35817<br>
      (205)368-2941
    </address>
    <div class="side-band"></div>
  </section>

  <h1 class="title">LETTERHEAD<br>+<br>ENVELOPE</h1>
  <p class="tagline">Professional, Serious, Minimal Design</p>

</main>
</body>
</html>
```